Beauty Clinic Treatment Menu (Lumen Nails & Beauty)

Needing a treatment menu designed for a beauty clinic in Whitianga, New Zealand. Like the colours grey, pink, white.
Elegant, Modern and feminine

Lumen Nails & Beauty
Karen Pell
Room3, 48 Fernleaf Lane
Whitianga
0273816240
Karen.lumen@mailbox.test
lumenbeauty.co.nz

Target Market(s)

Females

Industry/Entity Type

Beauty Salon

Font styles to use
Serif

Colors

Requirements
Must have
• Chatterly and Snapgrid logo

```html
<!DOCTYPE html>
<html lang="en">
<head>
<meta charset="utf-8">
<title>Lumen Nails &amp; Beauty – Treatment Menu</title>
<link rel="stylesheet" href="https://fonts.googleapis.com/css2?family=Pinyon+Script&family=Work+Sans:wght@300;400&display=swap">
<style>
  :root {
    --backdrop: #bdb1aa;
    --paper: #fbfbfb;
    --marble: #ebebeb;
    --accent: #a67f6f;
    --leader: #c9b2a7;
  }
  * { box-sizing: border-box; margin: 0; padding: 0; }
  html, body { width: 1200px; height: 882px; overflow: hidden; }
  body {
    background: var(--backdrop);
    font-family: "Work Sans", sans-serif;
    color: var(--accent);
    position: relative;
  }
  .menu-card {
    position: absolute;
    left: 320px; top: 8px;
    width: 560px; height: 865px;
    background: var(--paper);
    box-shadow: 0 2px 10px rgba(0,0,0,.12);
    overflow: hidden;
  }
  .marble-texture {
    position: absolute; inset: 0;
    background:
      radial-gradient(ellipse 60% 40% at 30% 20%, var(--marble), transparent 70%),
      radial-gradient(ellipse 50% 35% at 75% 55%, var(--marble), transparent 70%),
      radial-gradient(ellipse 55% 30% at 40% 85%, var(--marble), transparent 70%),
      var(--paper);
  }
  .menu-title {
    position: absolute; left: 0; right: 0; top: 58px;
    text-align: center;
    font-family: "Pinyon Script", cursive;
    font-size: 62px; line-height: 1; font-weight: 400;
    color: var(--accent);
  }
  .column {
    position: absolute; top: 163px;
    font-size: 10px; line-height: 11.9px; font-weight: 400;
    letter-spacing: .2px;
  }
  .column-left { left: 24.5px; width: 240px; }
  .column-right { left: 303px; width: 232px; }
  .section-heading {
    height: 35px; line-height: 35px;
    font-size: 21px; font-weight: 300; letter-spacing: .5px;
    margin-left: -0.5px;
  }
  .group-label { text-transform: uppercase; }
  .row { display: flex; align-items: baseline; }
  .row .leader {
    flex: 1; border-bottom: 1px dotted var(--leader);
    margin: 0 1px; transform: translateY(-2px);
  }
  .row .price { white-space: nowrap; }
  .column-left .row .price { width: 50px; }
  .column-right .row .price { width: 37px; }
  .gap { height: 11.9px; }
  .badge-art {
    position: absolute; left: 258px; top: 738px;
    width: 44px; height: 46px; border-radius: 50%;
    background: radial-gradient(circle, rgba(166,127,111,.25), transparent 70%);
  }
  .contact-bar {
    position: absolute; top: 798px; left: 0; right: 0; height: 30px;
  }
  .contact-item {
    position: absolute; top: 0; transform: translateX(-50%);
    text-align: center; font-size: 7.6px; white-space: nowrap;
  }
  .contact-item svg { display: block; margin: 0 auto 4px; width: 10px; height: 10px; }
</style>
</head>
<body>
  <main class="menu-card">
    <div class="marble-texture" role="img" aria-label="Soft white and grey marble texture"></div>

    <h1 class="menu-title">Menu</h1>

    <section class="column column-left">
      <h2 class="section-heading">NAILS</h2>
      <p class="group-label">Manicure</p>
      <div class="gap"></div>
      <div class="row"><span>Gel Polish</span><span class="leader"></span><span class="price">$45</span></div>
      <div class="row"><span>Regular Polish</span><span class="leader"></span><span class="price">$40</span></div>
      <div class="gap"></div>
      <p class="group-label">Pedicure</p>
      <div class="gap"></div>
      <div class="row"><span>Gel Polish</span><span class="leader"></span><span class="price">$45</span></div>
      <div class="row"><span>Regular Polish</span><span class="leader"></span><span class="price">$40</span></div>
      <div class="gap"></div>
      <p class="group-label">Luxury Pedicure</p>
      <div class="gap"></div>
      <p>Includes: soak, exfoliation,<br>heel rasping and massage.</p>
      <div class="gap"></div>
      <div class="row"><span>Gel Polish</span><span class="leader"></span><span class="price">$60</span></div>
      <div class="row"><span>Regular Polish</span><span class="leader"></span><span class="price">$55</span></div>
      <div class="gap"></div>
      <div class="row"><span class="group-label">Gel Removal and Nail Tidy</span><span style="flex:1"></span><span class="price">$25</span></div>
      <div class="gap"></div>
      <p class="group-label">Add On</p>
      <div class="gap"></div>
      <div class="row"><span>Gel Removal</span><span class="leader"></span><span class="price">$5</span></div>
      <div class="row"><span>Nail Strengthener</span><span class="leader"></span><span class="price">$5/ layer</span></div>
      <div class="row"><span>Builder gel overlay</span><span class="leader"></span><span class="price">$10</span></div>
      <div class="row"><span>Nail Art/ Glitter</span><span class="leader"></span><span class="price">$POA</span></div>

      <h2 class="section-heading">FACE</h2>
      <div class="row"><span>Lip</span><span class="leader"></span><span class="price">$15</span></div>
      <div class="row"><span>Chin</span><span class="leader"></span><span class="price">$15</span></div>

      <h2 class="section-heading">BODY</h2>
      <div class="row"><span>Under Arm</span><span class="leader"></span><span class="price">$20</span></div>
      <div class="row"><span>1/2 Leg</span><span class="leader"></span><span class="price">$35</span></div>
      <div class="row"><span>Full Leg</span><span class="leader"></span><span class="price">$55</span></div>
      <div class="row"><span>1/2 Arm</span><span class="leader"></span><span class="price">$30</span></div>
      <div class="row"><span>Full Arm</span><span class="leader"></span><span class="price">$40</span></div>
      <div class="row"><span>Bikini</span><span class="leader"></span><span class="price">$28</span></div>
      <div class="row"><span>Extended Bikini</span><span class="leader"></span><span class="price">$38</span></div>
      <div class="row"><span>Brazilian (1st Time)</span><span class="leader"></span><span class="price">$65</span></div>
      <div class="row"><span>Brazilian (4-6 Weeks)</span><span class="leader"></span><span class="price">$50</span></div>
      <div class="row"><span>Patches</span><span class="leader"></span><span class="price">$5</span></div>
    </section>

    <section class="column column-right">
      <h2 class="section-heading">FACIALS</h2>
      <div class="row"><span>Deep Cleansing Facial</span><span class="leader"></span><span class="price">$75</span></div>
      <div class="gap"></div>
      <p>45 Minutes</p>
      <div class="gap"></div>
      <p>Removes build up of skin<br>cells, leaves the skin feeling<br>soft and hydrated.</p>
      <div class="gap"></div>
      <div class="row"><span>Therapeutic Facial</span><span class="leader"></span><span class="price">$105</span></div>
      <div class="gap"></div>
      <p>60 Minutes</p>
      <div class="gap"></div>
      <p>Tailored to suit your skin’s<br>specific needs.</p>
      <div class="gap"></div>
      <div class="row"><span>Rejuvenation Facial</span><span class="leader"></span><span class="price">$120</span></div>
      <div class="gap"></div>
      <p>60 Minutes</p>
      <div class="gap"></div>
      <p>Active yet gentle treatment<br>that facilitates dermal<br>rejuvenation.</p>
      <div class="gap"></div>
      <div class="row"><span>35% Glycolic Facial</span><span class="leader"></span><span class="price">$120</span></div>
      <div class="gap"></div>
      <p>60 Minutes</p>
      <div class="gap"></div>
      <p>Hydrating, deep exfoliation<br>treatment that improves skin<br>texture and appearance.</p>
      <div class="gap"></div>
      <div class="row"><span>Dermaplaning</span><span class="leader"></span><span class="price">$120</span></div>
      <div class="gap"></div>
      <p>Creates a smooth and radiant<br>skin surface. Also removs soft<br>facial hairs.</p>

      <h2 class="section-heading">EYES</h2>
      <div class="row"><span>Silken Lash Lift</span><span class="leader"></span><span class="price">$115</span></div>
      <div class="row"><span>Eyebrow Shape</span><span class="leader"></span><span class="price">$19</span></div>
      <div class="row"><span>Eyebrow Tint</span><span class="leader"></span><span class="price">$18</span></div>
      <div class="row"><span>Eyelash Tint</span><span class="leader"></span><span class="price">$25</span></div>
      <div class="row"><span>Eye Trio</span><span class="leader"></span><span class="price">$45</span></div>
    </section>

    <div class="badge-art" role="img" aria-label="Small line illustration of beauty tools"></div>

    <footer class="contact-bar">
      <div class="contact-item" style="left:69px">
        <svg viewBox="0 0 10 10" fill="none" stroke="currentColor" stroke-width=".8"><path d="M5 9.3S1.8 6 1.8 4a3.2 3.2 0 0 1 6.4 0C8.2 6 5 9.3 5 9.3z"/><circle cx="5" cy="4" r="1.1"/></svg>
        Room3, 48 Fernleaf Lane
      </div>
      <div class="contact-item" style="left:232px">
        <svg viewBox="0 0 10 10" fill="none" stroke="currentColor" stroke-width=".8"><path d="M2.2 1h1.6l.8 2-1 .8a5.5 5.5 0 0 0 2.6 2.6l.8-1 2 .8v1.6c0 .6-.5 1-1 1A7.8 7.8 0 0 1 1.2 2c0-.5.4-1 1-1z"/></svg>
        0273 816 240
      </div>
      <div class="contact-item" style="left:353px">
        <svg viewBox="0 0 10 10" fill="none" stroke="currentColor" stroke-width=".8"><rect x="1" y="2.3" width="8" height="5.6"/><path d="M1 2.3l4 3.4 4-3.4M1 7.9l3-2.8M9 7.9L6 5.1"/></svg>
        Karen.lumen@mailbox.test
      </div>
      <div class="contact-item" style="left:482px">
        <svg viewBox="0 0 10 10" fill="none" stroke="currentColor" stroke-width=".8"><circle cx="5" cy="5" r="4"/><path d="M1 5h8M5 1c-2 2.4-2 5.6 0 8M5 1c2 2.4 2 5.6 0 8"/></svg>
        lumenbeauty.co.nz
      </div>
    </footer>
  </main>
</body>
</html>
```